Website for keystone mobile detailing.

Need a homepage, pages for: car and truck detailing, boat detailing, airplane detailing, about us, contact us. I have the domain name through nimbuspark so I will need the design uploaded on my domain. Also hoping to link other domains to this page.I would like to see the logo more pronounced. I would like to see a large phone number link to call my business. The layout looks nice but the pics need to depict car washing and waxing not car mechanics. i would like the colors of the webpage to incorporate the colors found in the logo in some way. I would like links to social media pages

Target Market(s)

Local customers in Vero Beach, Florida.

Number of Pages Required

5+ page

Colors

Designer to choose colors to be used in the design.

Requirements
Must have
• Easy to navigate, attractive pages with pictures and logo, professional looking. must have my phone number and logo very prevalent and links to call or go to home page. I would like links to my social media accounts on the home page.
Nice to have
• Easy to navigate, attractive pages with pictures and logo, professional looking.

```html
<!DOCTYPE html>
<html lang="en">
<head>
<meta charset="utf-8">
<title>Keystone Mobile Detailing</title>
<link href="https://fonts.googleapis.com/css2?family=Maven+Pro:wght@500;700&family=Open+Sans:wght@400;600;700&display=swap" rel="stylesheet">
<style>
:root{
  --navy:#1c2380;
  --red:#e8202a;
  --cyan:#0aa5e0;
  --ink:#222;
  --muted:#666;
  --light:#f2f2f2;
  --map:#f5f5f5;
  --footer:#232323;
  --footer-text:#bdbdbd;
  --line:#e3e3e3;
  --hero-dark:#3f3d38;
  --hero-mid:#9c968a;
  --hero-light:#e7e3da;
  --hero-car:#f4f2ee;
}
*{margin:0;padding:0;box-sizing:border-box}
html,body{width:1200px;height:2560px;overflow:hidden;background:#fff}
body{position:relative;font-family:"Open Sans",Arial,sans-serif;color:var(--ink)}
.abs{position:absolute}
.heading{font-family:"Maven Pro","Open Sans",sans-serif;font-weight:700}

/* header */
.top-email{left:160px;top:46px;font-size:12px;color:var(--cyan)}
.brand{left:465px;top:14px;width:270px;height:80px;display:flex;align-items:center;gap:12px}
.brand-dot{width:46px;height:46px;border-radius:50%;background:var(--red);flex:none}
.brand-name{font-family:"Maven Pro",sans-serif;font-weight:700;font-size:23px;line-height:1.05;color:var(--navy)}
.call-box{left:801px;top:31px;height:42px;display:flex;border:1px solid var(--line)}
.call-icon{width:42px;background:var(--cyan);display:flex;align-items:center;justify-content:center}
.call-num{width:196px;display:flex;align-items:center;justify-content:center;font-family:"Maven Pro",sans-serif;font-weight:700;font-size:23px;letter-spacing:1px}
.nav{left:0;top:102px;width:1200px;height:66px;border-top:1px solid var(--line)}
.nav-active{left:160px;top:102px;width:187px;height:2px;background:var(--cyan)}
.nav a{position:absolute;top:25px;font-size:11px;font-weight:600;color:var(--ink);text-decoration:none;letter-spacing:.4px}
.social-top{right:160px;top:126px;display:flex;gap:18px}
.social-top span{width:15px;height:15px;border-radius:3px;display:block}

/* hero: soft tonal field of a worker washing a white car in a garage */
.hero{left:0;top:168px;width:1200px;height:450px;
  background:
    radial-gradient(ellipse 160px 260px at 190px 300px, rgba(70,68,62,.85) 0%, rgba(70,68,62,.45) 55%, rgba(70,68,62,0) 100%),
    radial-gradient(ellipse 90px 120px at 150px 120px, rgba(150,50,45,.45) 0%, rgba(150,50,45,0) 100%),
    radial-gradient(ellipse 420px 260px at 1000px 230px, var(--hero-car) 0%, rgba(235,232,226,.7) 50%, rgba(235,232,226,0) 100%),
    radial-gradient(ellipse 120px 90px at 1120px 400px, rgba(40,40,40,.55) 0%, rgba(40,40,40,0) 100%),
    radial-gradient(ellipse 110px 80px at 840px 400px, rgba(45,45,45,.5) 0%, rgba(45,45,45,0) 100%),
    linear-gradient(180deg, rgba(0,0,0,0) 0%, rgba(0,0,0,0) 62%, rgba(120,112,98,.35) 100%),
    linear-gradient(100deg, var(--hero-dark) 0%, var(--hero-mid) 22%, var(--hero-light) 48%, #d9d4ca 75%, #cfcac0 100%);}
.hero-title{right:159px;top:340px;text-align:right;font-size:46px;color:var(--navy)}
.hero-sub{right:159px;top:402px;text-align:right;font-size:31px;font-weight:500;color:var(--red);font-family:"Maven Pro",sans-serif}

/* about */
.about-title{left:0;width:1200px;top:708px;text-align:center;font-size:29px;color:var(--navy)}
.about-title em{font-style:normal;color:var(--red)}
.about-sub{left:0;width:1200px;top:789px;text-align:center;font-size:12px;color:var(--cyan)}
.about-photo{left:0;top:840px;width:439px;height:253px;
  background:
    radial-gradient(ellipse 50px 80px at 265px 185px, rgba(230,100,30,.85) 0%, rgba(230,100,30,0) 100%),
    radial-gradient(ellipse 130px 110px at 90px 140px, rgba(225,228,230,.9) 0%, rgba(225,228,230,0) 100%),
    linear-gradient(180deg,#8e8e8e 0%,#b8302b 12%,#c63b33 30%,#d7d7d7 42%,#7b7b7b 70%,#4f4f4f 100%);}
.thumb{top:1101px;width:87px;height:58px}
.thumb.active{outline:3px solid var(--cyan)}
.about-text{left:486px;top:840px;width:556px;font-size:12px;line-height:22px;color:var(--muted)}
.boat-icon{left:488px;top:983px;width:90px;height:40px;border-radius:6px;background:var(--cyan)}
.boat-label{left:486px;top:1051px;font-size:13px;font-weight:600}
.ticks{left:486px;top:1088px;list-style:none;font-size:12px;color:var(--muted)}
.ticks li{display:flex;align-items:center;gap:12px;height:28px}

/* call band */
.call-band{left:0;top:1231px;width:1200px;height:121px;background:var(--light);display:flex;align-items:center;justify-content:center;gap:18px;font-family:"Maven Pro",sans-serif;font-weight:700;font-size:22px}
.call-band .num{border:2px solid var(--red);color:var(--red);padding:4px 16px;letter-spacing:1px}

/* services */
.services{left:0;top:1352px;width:1200px;height:432px;
  background:
    radial-gradient(ellipse 260px 200px at 800px 180px, rgba(120,120,120,.55) 0%, rgba(120,120,120,0) 100%),
    radial-gradient(ellipse 200px 160px at 1050px 300px, rgba(90,90,90,.5) 0%, rgba(90,90,90,0) 100%),
    radial-gradient(ellipse at 70% 50%,#4a4a4a 0%,#262626 60%,#161616 100%);}
.services-title{left:0;width:1200px;top:1426px;text-align:center;font-size:27px;color:#fff}
.services-rule{left:570px;top:1470px;width:60px;height:1px;background:#888}
.services-sub{left:0;width:1200px;top:1505px;text-align:center;font-size:12px;color:#eee}
.svc{width:110px;height:110px;border:3px solid #fff;border-radius:50%;top:1568px;display:flex;align-items:center;justify-content:center}
.svc-art{width:60px;height:44px;border-radius:8px;background:#bfbfbf}
.svc-label{top:1698px;width:240px;text-align:center;font-size:14px;font-weight:700;letter-spacing:1px;color:#fff}
.svc-next{top:1596px;width:54px;height:54px;border-radius:50%;border:2px solid #aaa;display:flex;align-items:center;justify-content:center}

/* partners */
.partners-title{left:0;width:1200px;top:1832px;text-align:center;font-size:27px;color:var(--navy)}
.partners-title em{font-style:normal;color:var(--red)}
.partners-rule{left:570px;top:1878px;width:60px;height:1px;background:#ccc}
.partner{top:1910px;width:110px;height:30px;background:#2b2b2b;border-radius:4px}
.map-band{left:0;top:2009px;width:1200px;height:74px;background:var(--map);text-align:center}
.map-band span{display:block;margin-top:45px;font-size:9px;letter-spacing:1px;color:#999}

/* footer */
.footer{left:0;top:2083px;width:1200px;height:477px;background:var(--footer)}
.f-head{top:2134px;font-size:12px;font-weight:700;letter-spacing:.5px;color:#fff}
.f-text{left:160px;top:2184px;width:220px;font-size:11px;line-height:22px;color:var(--footer-text)}
.f-brand{left:160px;top:2282px;display:flex;align-items:center;gap:10px}
.f-brand .dot{width:36px;height:36px;border-radius:50%;background:#fff}
.f-brand .name{font-family:"Maven Pro",sans-serif;font-weight:700;font-size:18px;line-height:1.05;color:#fff}
.f-nav{left:493px;top:2184px;list-style:none;font-size:11px;line-height:22px;color:var(--footer-text)}
.f-input{left:691px;top:2190px;width:349px;height:80px;border:1px solid #555}
.f-btn{left:691px;top:2285px;width:107px;height:37px;border:1px solid #777;color:#fff;font-size:10px;font-weight:700;letter-spacing:1px;display:flex;align-items:center;justify-content:center}
.f-rule{left:160px;top:2395px;width:880px;height:1px;background:#3d3d3d}
.f-social{left:531px;top:2447px;display:flex;gap:26px}
.f-social span{width:14px;height:14px;border-radius:50%;background:#cfcfcf;display:block}
.copy{left:0;width:1200px;top:2494px;text-align:center;font-size:10px;color:var(--footer-text)}
</style>
</head>
<body>

<header>
  <div class="abs top-email">info@keystonemobiledetailing.com</div>
  <div class="abs brand"><span class="brand-dot"></span><span class="brand-name">Keystone<br>Mobile Detailing</span></div>
  <div class="abs call-box">
    <div class="call-icon"><svg width="18" height="18" viewBox="0 0 24 24"><path fill="#fff" d="M6.6 10.8a15.1 15.1 0 0 0 6.6 6.6l2.2-2.2c.3-.3.7-.4 1-.2 1.1.4 2.3.6 3.6.6.6 0 1 .4 1 1V20c0 .6-.4 1-1 1A17 17 0 0 1 3 4c0-.6.4-1 1-1h3.5c.6 0 1 .4 1 1 0 1.3.2 2.5.6 3.6.1.3 0 .7-.2 1z"/></svg></div>
    <div class="call-num">772-555-0148</div>
  </div>
  <nav class="abs nav">
    <a style="left:179px">HOME</a>
    <a style="left:256px">ABOUT US</a>
    <a style="left:355px">SERVICES</a>
    <a style="left:447px">CLIENTS</a>
    <a style="left:536px">CONTACT US</a>
  </nav>
  <div class="abs nav-active"></div>
  <div class="abs social-top">
    <span style="background:#3b5b98"></span><span style="background:#2ba3e1"></span><span style="background:#c7915a"></span>
  </div>
</header>

<section>
  <div class="abs hero" role="img" aria-label="Photo of a worker in grey overalls pressure-washing a white car inside a bright garage"></div>
  <h1 class="abs heading hero-title">From 30 Years We Provided</h1>
  <p class="abs hero-sub">Cars, Boats, and Airplanes  Wash Service</p>
</section>

<section>
  <h2 class="abs heading about-title"><em>Who Is Keystone</em> Mobile Detailing</h2>
  <p class="abs about-sub">Cars, Boats, And Airplanes Wash &amp; Detailing</p>
  <div class="abs about-photo" role="img" aria-label="Photo of a worker in orange overalls pressure-washing a red boat hull"></div>
  <div class="abs thumb active" style="left:160px;background:linear-gradient(#b34a42,#8d8d8d)" role="img" aria-label="Thumbnail of boat washing"></div>
  <div class="abs thumb" style="left:254px;background:linear-gradient(#d8b27a,#8f8f8f)" role="img" aria-label="Thumbnail of car washing"></div>
  <div class="abs thumb" style="left:350px;background:linear-gradient(#b7c4d2,#7d8590)" role="img" aria-label="Thumbnail of airplane washing"></div>
  <p class="abs about-text">Lorem ipsum dolor sit amet, consectetur adipiscing elit, sed do eiusmod tempor incididunt ut labore et dolore magna aliqua. Ut enim ad minim veniam, quis nostrud exercitation ullamco laboris nisi ut aliquip ex ea commodo consequat. Duis aute irure dolor in reprehenderit in voluptate velit esse cillum dolore eu fugiat nulla pariatur. Excepteur sint occaecat cupidatat non proident, sunt in culpa qui officia deserunt mollit anim id est laborum.</p>
  <div class="abs boat-icon" role="img" aria-label="Boat icon"></div>
  <h3 class="abs boat-label">BOAT WASH</h3>
  <ul class="abs ticks">
    <li><svg width="10" height="10" viewBox="0 0 10 10"><path d="M1 5l3 3 5-7" stroke="var(--cyan)" stroke-width="2" fill="none"/></svg>Lorem ipsum dolor sit amet, consecteturelit,</li>
    <li><svg width="10" height="10" viewBox="0 0 10 10"><path d="M1 5l3 3 5-7" stroke="var(--cyan)" stroke-width="2" fill="none"/></svg>Sed do eiusmod tempor</li>
  </ul>
</section>

<section class="abs call-band">
  <span>My cell number is</span><span class="num">772-555-0148</span><span>Please feel free to call for free estimates.</span>
</section>

<section>
  <div class="abs services" role="img" aria-label="Dark close-up photo of a wet car headlight"></div>
  <h2 class="abs heading services-title">Our Services</h2>
  <div class="abs services-rule"></div>
  <p class="abs services-sub">Cars, Boats, And Airplanes Wash and Detailings Services</p>
  <div class="abs svc" style="left:223px"><div class="svc-art" role="img" aria-label="Car wash icon"></div></div>
  <div class="abs svc" style="left:544px"><div class="svc-art" role="img" aria-label="Boat wash icon"></div></div>
  <div class="abs svc" style="left:870px"><div class="svc-art" role="img" aria-label="Airplane wash icon"></div></div>
  <div class="abs svc-next" style="left:413px"><svg width="14" height="14" viewBox="0 0 14 14"><path d="M5 2l5 5-5 5" stroke="#fff" stroke-width="1.5" fill="none"/></svg></div>
  <div class="abs svc-next" style="left:736px"><svg width="14" height="14" viewBox="0 0 14 14"><path d="M5 2l5 5-5 5" stroke="#fff" stroke-width="1.5" fill="none"/></svg></div>
  <div class="abs svc-label" style="left:158px">CAR WASH</div>
  <div class="abs svc-label" style="left:479px">BOAT WASH</div>
  <div class="abs svc-label" style="left:805px">AIRPLANES WASH</div>
</section>

<section>
  <h2 class="abs heading partners-title"><em>Our</em> Partners</h2>
  <div class="abs partners-rule"></div>
  <div class="abs partner" style="left:163px"></div>
  <div class="abs partner" style="left:360px"></div>
  <div class="abs partner" style="left:539px"></div>
  <div class="abs partner" style="left:744px"></div>
  <div class="abs partner" style="left:928px"></div>
  <div class="abs map-band">
    <svg class="abs" style="left:594px;top:22px" width="12" height="14" viewBox="0 0 12 14"><path d="M6 1a4 4 0 0 0-4 4c0 3 4 8 4 8s4-5 4-8a4 4 0 0 0-4-4z" stroke="#999" fill="none"/><circle cx="6" cy="5" r="1.3" fill="#999"/></svg>
    <span>SHOW MAP</span>
  </div>
</section>

<footer>
  <div class="abs footer"></div>
  <h4 class="abs f-head" style="left:160px">ABOUT</h4>
  <h4 class="abs f-head" style="left:493px">NAVIGATION</h4>
  <h4 class="abs f-head" style="left:691px">NEWSLETTER</h4>
  <p class="abs f-text">Lorem ipsum dolor sit amet, consectetur adipiscing elit, sed do eiusmod tempor incididunt ut labore et dolore magna</p>
  <div class="abs f-brand"><span class="dot"></span><span class="name">Keystone<br>Mobile Detailing</span></div>
  <ul class="abs f-nav"><li>Home</li><li>About Us</li><li>Services</li><li>Clients</li><li>Contact Us</li></ul>
  <div class="abs f-input"></div>
  <div class="abs f-btn">SUBSCRIBE</div>
  <div class="abs f-rule"></div>
  <div class="abs f-social"><span></span><span></span><span></span><span></span></div>
  <p class="abs copy">© Copyright 2018 Keystone Mobile Detailing. All Rights Reserved.</p>
</footer>

</body>
</html>
```